Redbrook Disposal ~ A+ Division of Ironclad

Energetic ,different ,exotic ,modern,
never before done, next level buisness card for a trash dumpster company
is for a trash removal construction company ...please have your wildest ideas i dont want a boring basic buisness card i want people to say wow !! And be able to mention you and who designed my card ...i know you take pride in your work i do to ....3 years ago quietfern from pixel harbor made a logo for me and i still love it .....use his colors and the word ironclad DO NOT USE ROOFING AND REMODELING use Redbrook Disposal ....look at his Logo i Like the [I] LOGO and word Ironclad ....you surprise me and we will do alot more projects with you and or pixel harbor ....thank you for your hard work and your time i do appreciate all of you and admire your skills designing .....i really do appreciate all of you thank you -dale
Ps Lets make these biz cards special different from many ,unique

Target Market(s)

Construction .....dumpsters trash Trash removal

Industry/Entity Type

Construction

Contact Information for Business Card

Black gold white maybe more colors

Requirements
Must have
• Ironclad ~Redbrook Disposal division Serving Atlanta and surrounding areas'Chief executive Dale Kimber cell 404 555 0172 Office 404 888 8888Follow us on fb ,instagram .. info@Redbrookdisposal.example Redbrookdisposal.example Hablamos espaƱol
Nice to have
• Black gold white colors like my logo i updated and you can add more if you want ....its a construction / trucking company dumpster Trash company we recycle also
Should not have
• When you look at my logo (Must not have roofing and remodeling )

```html
<!DOCTYPE html>
<html lang="en">
<head>
<meta charset="utf-8">
<title>Ironclad – Business Card</title>
<link href="https://fonts.googleapis.com/css2?family=Work+Sans:wght@400;500;700&display=swap" rel="stylesheet">
<style>
  :root {
    --page-bg: #e6ddd2;
    --card-bg: #2e2b29;
    --card-edge: #3a3633;
    --gold: #d6a21e;
    --gold-soft: #c9962a;
    --silver: #dcd9d4;
    --muted: #bdb7ae;
    --frost: rgba(120, 112, 104, 0.35);
  }
  * { margin: 0; padding: 0; box-sizing: border-box; }
  html, body {
    width: 1200px; height: 1047px; overflow: hidden;
    background: var(--page-bg);
    font-family: "Work Sans", Arial, sans-serif;
  }
  .business-card {
    position: absolute;
    left: 54px; top: 289px;
    width: 944px; height: 515px;
    border-radius: 22px;
    background: var(--card-bg);
    border: 1px solid var(--card-edge);
    overflow: hidden;
  }
  .frost-band {
    position: absolute;
    left: 290px; top: 0; width: 100px; height: 100%;
    background: linear-gradient(90deg, transparent 0%, var(--frost) 40%, var(--frost) 60%, transparent 100%);
  }
  .brand {
    position: absolute; left: 58px; top: 46px;
    display: flex; align-items: center; gap: 14px;
  }
  .brand-square { width: 96px; height: 91px; background: var(--gold); }
  .brand-name {
    font-weight: 700; font-size: 44px; letter-spacing: 2px;
    color: var(--silver); text-transform: uppercase;
  }
  .division-line {
    position: absolute; left: 58px; top: 152px;
    font-size: 15px; font-weight: 500; letter-spacing: 1.5px;
    color: var(--gold-soft); text-transform: uppercase;
  }
  .brand-block {
    position: absolute; left: 577px; top: 54px;
    width: 313px; height: 398px; background: var(--gold);
  }
  .service-notes {
    position: absolute; right: 54px; top: 464px;
    text-align: right; font-size: 15px; line-height: 20px;
    color: var(--muted); letter-spacing: 0.5px;
  }
  .service-notes .accent { color: var(--gold-soft); }
  .contact { position: absolute; left: 56px; top: 280px; }
  .person-name {
    font-weight: 500; font-size: 31px; color: var(--gold-soft);
    letter-spacing: 0.5px; text-transform: uppercase; line-height: 36px;
  }
  .person-title {
    font-size: 21px; color: var(--muted); margin-top: 2px; letter-spacing: 0.5px; line-height: 26px;
  }
  .contact-list { list-style: none; margin-top: 18px; }
  .contact-list li {
    display: flex; align-items: center; gap: 12px;
    font-size: 20px; color: var(--muted); letter-spacing: 1px;
    height: 29px;
  }
  .contact-list svg { width: 14px; height: 14px; flex: none; fill: none; stroke: var(--gold-soft); stroke-width: 1.6; }
</style>
</head>
<body>
  <div class="business-card">
    <div class="frost-band" role="img" aria-label="Frosted clear strip across the card"></div>

    <div class="brand">
      <div class="brand-square"></div>
      <div class="brand-name">Ironclad</div>
    </div>
    <div class="division-line">Redbrook Disposal ~ A division of Ironclad</div>

    <div class="brand-block"></div>

    <div class="service-notes">
      Serving Atlanta &amp; surrounding areas<br>
      Follow us on social · <span class="accent">Hablamos español</span>
    </div>

    <div class="contact">
      <div class="person-name">Dale Kimber</div>
      <div class="person-title">Chief executive</div>
      <ul class="contact-list">
        <li>
          <svg viewBox="0 0 14 14"><rect x="3.5" y="1" width="7" height="12" rx="1.2"/><line x1="6" y1="11" x2="8" y2="11"/></svg>
          404 555 0172
        </li>
        <li>
          <svg viewBox="0 0 14 14"><path d="M3 1.5 L5.5 1.5 L6.5 4.5 L5 5.8 C5.8 7.6 6.6 8.4 8.2 9.2 L9.5 7.7 L12.5 8.7 L12.5 11.2 C12.5 12 11.8 12.6 11 12.5 C6 12 2 8 1.5 3 C1.4 2.2 2.1 1.5 3 1.5 Z"/></svg>
          4045550139
        </li>
        <li>
          <svg viewBox="0 0 14 14"><rect x="1.5" y="3" width="11" height="8" rx="1"/><path d="M1.5 3.5 L7 8 L12.5 3.5"/></svg>
          info@Redbrookdisposal.example
        </li>
        <li>
          <svg viewBox="0 0 14 14"><circle cx="7" cy="7" r="5.5"/><ellipse cx="7" cy="7" rx="2.3" ry="5.5"/><line x1="1.5" y1="7" x2="12.5" y2="7"/></svg>
          www.Redbrookdisposal.example
        </li>
      </ul>
    </div>
  </div>
</body>
</html>
```